Update the A4 Specials Page for Restaurant/Cafe

Provide a MINIMALIST attractive Specials page we can print weekly for our food and drink specials to give to our guests. Final design is to be provided in WORD Document so it can be easily edited by Manager. Should be black text and MINIMALIST to minimise ink usage as we print hundreds a week. We have UPLOADED the existing page as a template for you to update. Maybe logo can stay, see what you think. Or delete it and do something else. Keep it simple. Choose a good FONT. Could be a little playful with a cocktail ICON or something. Our existing menus can be seen at www.tallowmillcafe.com.au and they are using font Alegreya. Please note we are unable to provide any feedback to designers, however we really do appreciate your time if you are submitting a design. Thank you for your participation.

```html
<!DOCTYPE html>
<html lang="en">
<head>
<meta charset="utf-8">
<title>Tallow Mill Cafe – Weekly Specials</title>
<link rel="stylesheet" href="https://fonts.googleapis.com/css2?family=Alegreya+Sans:wght@700;800&family=Roboto:wght@400&display=swap">
<style>
  :root {
    --rust: #b5541f;
    --navy: #1d3a8a;
    --ink: #111111;
    --paper: #ffffff;
    --backdrop: #ffffff;
  }
  * { margin: 0; padding: 0; box-sizing: border-box; }
  html, body { width: 1200px; height: 1000px; overflow: hidden; background: var(--backdrop); }
  .canvas { position: relative; width: 1200px; height: 1000px; }
  .sheet {
    position: absolute; left: 76px; top: 120px; width: 1048px; height: 740px;
    background: var(--paper);
    box-shadow: 0 14px 30px rgba(0,0,0,0.28);
  }
  .page { position: absolute; top: 144px; width: 476px; height: 694px; }
  .page--left { left: 100px; }
  .page--right { left: 624px; }
  .page-frame { position: absolute; inset: 0; }

  .brand-box, .title-box {
    position: absolute; top: 36px; height: 73px;
    border: 2px solid var(--rust);
    display: flex; align-items: center; justify-content: center; text-align: center;
    font-family: "Alegreya Sans", sans-serif; font-weight: 800; color: var(--navy);
  }
  .brand-box { left: 35px; width: 160px; font-size: 23px; line-height: 1.05; }
  .title-box { left: 197px; width: 246px; font-size: 21px; line-height: 1.1; font-weight: 700; }

  .item { position: absolute; left: 47px; width: 393px; height: 98px; }
  .item__icon {
    position: absolute; left: 0; top: 0; width: 86px; height: 98px;
    border: 2px solid var(--rust); border-radius: 9px;
    display: flex; align-items: center; justify-content: center;
  }
  .item__name {
    position: absolute; left: 102px; top: 16px;
    font-family: "Alegreya Sans", sans-serif; font-weight: 800; font-size: 17px;
    line-height: 22px; color: var(--ink);
  }
  .item__desc {
    position: absolute; left: 102px; width: 290px;
    font-family: "Roboto", sans-serif; font-size: 12.6px; line-height: 16px; color: var(--ink);
  }
  .item__price {
    position: absolute; right: 0; top: 1px; width: 65px; height: 29px;
    border: 1.5px solid var(--ink); border-radius: 8px;
    display: flex; align-items: center; justify-content: center;
    font-family: "Alegreya Sans", sans-serif; font-weight: 800; font-size: 15px; color: var(--ink);
  }
  .section-label {
    position: absolute;
    font-family: "Alegreya Sans", sans-serif; font-weight: 800; font-size: 11.5px; color: var(--ink);
  }
</style>
</head>
<body>
<div class="canvas">
  <div class="sheet"></div>

  <!-- Page template used twice -->
  <section class="page page--left">
    <svg class="page-frame" width="476" height="694" viewBox="0 0 476 694" fill="none" stroke="#b5541f" stroke-width="1.3">
      <rect x="1" y="1" width="18" height="18" fill="#b5541f" stroke="none"/>
      <rect x="457" y="1" width="18" height="18" fill="#b5541f" stroke="none"/>
      <rect x="1" y="674" width="18" height="18" fill="#b5541f" stroke="none"/>
      <rect x="457" y="674" width="18" height="18" fill="#b5541f" stroke="none"/>
      <line x1="33" y1="3" x2="443" y2="3"/>
      <line x1="75" y1="8" x2="400" y2="8"/>
      <line x1="75" y1="685" x2="400" y2="685"/>
      <line x1="33" y1="691" x2="443" y2="691"/>
      <line x1="4" y1="35" x2="4" y2="360"/>
      <line x1="18" y1="96" x2="18" y2="660"/>
      <line x1="4" y1="405" x2="4" y2="655"/>
      <line x1="472" y1="35" x2="472" y2="420"/>
      <line x1="458" y1="96" x2="458" y2="660"/>
      <line x1="472" y1="460" x2="472" y2="655"/>
    </svg>
    <div class="brand-box">TALLOW MILL<br>CAFE</div>
    <div class="title-box">WEEKLY<br>SPECIALS</div>

    <article class="item" style="top:140px">
      <div class="item__icon">
        <svg width="64" height="50" viewBox="0 0 64 50" fill="none" stroke="#b5541f" stroke-width="1.6" stroke-linecap="round">
          <circle cx="32" cy="6" r="3"/>
          <path d="M8 36 C8 20 20 10 32 10 C44 10 56 20 56 36 Z"/>
          <rect x="2" y="37" width="60" height="7" rx="3.5"/>
        </svg>
      </div>
      <h2 class="item__name">CHICKEN FILO</h2>
      <p class="item__desc" style="top:52px">Creamy Chicken with Pinenuts, wrapped in Filo Pastry. Served with Side Salad &amp; Zulu Sauce.</p>
      <div class="item__price">$24</div>
    </article>

    <article class="item" style="top:264px">
      <div class="item__icon">
        <svg width="60" height="58" viewBox="0 0 60 58" fill="none" stroke="#b5541f" stroke-width="1.6" stroke-linecap="round">
          <path d="M24 4 c-4 4 4 6 0 10 M30 2 c-4 4 4 6 0 12 M36 4 c-4 4 4 6 0 10"/>
          <path d="M4 26 H56 C54 38 46 44 30 44 C14 44 6 38 4 26 Z"/>
          <rect x="8" y="49" width="44" height="5" rx="2.5"/>
        </svg>
      </div>
      <h2 class="item__name">MINESTRONE SOUP</h2>
      <p class="item__desc" style="top:52px">Served with Garlic Bread.</p>
      <div class="item__price">$8</div>
    </article>

    <div class="section-label" style="left:45px;top:387px">COCKTAIL SPECIAL</div>
    <article class="item" style="top:409px">
      <div class="item__icon">
        <svg width="64" height="70" viewBox="0 0 64 70" fill="none" stroke="#b5541f" stroke-width="1.6" stroke-linecap="round">
          <line x1="10" y1="6" x2="36" y2="30"/>
          <circle cx="50" cy="20" r="6"/>
          <path d="M6 20 H50 L28 46 Z"/>
          <path d="M14 30 H42"/>
          <line x1="28" y1="46" x2="28" y2="64"/>
          <line x1="18" y1="65" x2="38" y2="65"/>
        </svg>
      </div>
      <h2 class="item__name">PASSIONISTA</h2>
      <p class="item__desc" style="top:45px">Vodka, Passionfruit Pulp, Mango Puree<br>Top up with Ginger &amp; Lemon Kombucha.</p>
      <div class="item__price">$17</div>
    </article>

    <div class="section-label" style="left:33px;top:530px">CRAFT BEER SPECIAL</div>
    <article class="item" style="top:553px">
      <div class="item__icon">
        <svg width="56" height="68" viewBox="0 0 56 68" fill="none" stroke="#b5541f" stroke-width="1.6" stroke-linecap="round" stroke-linejoin="round">
          <path d="M6 16 C2 12 6 4 12 6 C14 0 24 0 26 5 C30 1 38 3 37 9 C42 9 42 16 38 17 L38 22 M6 16 V64 H38 V17"/>
          <path d="M10 17 H34"/>
          <path d="M38 30 H46 C49 30 50 32 50 35 V50 C50 53 49 55 46 55 H38"/>
          <line x1="14" y1="28" x2="14" y2="58"/>
          <line x1="22" y1="28" x2="22" y2="58"/>
          <line x1="30" y1="28" x2="30" y2="58"/>
        </svg>
      </div>
      <h2 class="item__name" style="top:3px">SLY GECKO<br>FRUIT PUNCH</h2>
      <p class="item__desc" style="top:60px">Tropical Pale Ale - 4.8% Alc.</p>
      <div class="item__price">$10</div>
    </article>
  </section>

  <section class="page page--right">
    <svg class="page-frame" width="476" height="694" viewBox="0 0 476 694" fill="none" stroke="#b5541f" stroke-width="1.3">
      <rect x="1" y="1" width="18" height="18" fill="#b5541f" stroke="none"/>
      <rect x="457" y="1" width="18" height="18" fill="#b5541f" stroke="none"/>
      <rect x="1" y="674" width="18" height="18" fill="#b5541f" stroke="none"/>
      <rect x="457" y="674" width="18" height="18" fill="#b5541f" stroke="none"/>
      <line x1="33" y1="3" x2="443" y2="3"/>
      <line x1="75" y1="8" x2="400" y2="8"/>
      <line x1="75" y1="685" x2="400" y2="685"/>
      <line x1="33" y1="691" x2="443" y2="691"/>
      <line x1="4" y1="35" x2="4" y2="360"/>
      <line x1="18" y1="96" x2="18" y2="660"/>
      <line x1="4" y1="405" x2="4" y2="655"/>
      <line x1="472" y1="35" x2="472" y2="420"/>
      <line x1="458" y1="96" x2="458" y2="660"/>
      <line x1="472" y1="460" x2="472" y2="655"/>
    </svg>
    <div class="brand-box">TALLOW MILL<br>CAFE</div>
    <div class="title-box">WEEKLY<br>SPECIALS</div>

    <article class="item" style="top:140px">
      <div class="item__icon">
        <svg width="64" height="50" viewBox="0 0 64 50" fill="none" stroke="#b5541f" stroke-width="1.6" stroke-linecap="round">
          <circle cx="32" cy="6" r="3"/>
          <path d="M8 36 C8 20 20 10 32 10 C44 10 56 20 56 36 Z"/>
          <rect x="2" y="37" width="60" height="7" rx="3.5"/>
        </svg>
      </div>
      <h2 class="item__name">CHICKEN FILO</h2>
      <p class="item__desc" style="top:52px">Creamy Chicken with Pinenuts, wrapped in Filo Pastry. Served with Side Salad &amp; Zulu Sauce.</p>
      <div class="item__price">$24</div>
    </article>

    <article class="item" style="top:264px">
      <div class="item__icon">
        <svg width="60" height="58" viewBox="0 0 60 58" fill="none" stroke="#b5541f" stroke-width="1.6" stroke-linecap="round">
          <path d="M24 4 c-4 4 4 6 0 10 M30 2 c-4 4 4 6 0 12 M36 4 c-4 4 4 6 0 10"/>
          <path d="M4 26 H56 C54 38 46 44 30 44 C14 44 6 38 4 26 Z"/>
          <rect x="8" y="49" width="44" height="5" rx="2.5"/>
        </svg>
      </div>
      <h2 class="item__name">MINESTRONE SOUP</h2>
      <p class="item__desc" style="top:52px">Served with Garlic Bread.</p>
      <div class="item__price">$8</div>
    </article>

    <div class="section-label" style="left:45px;top:387px">COCKTAIL SPECIAL</div>
    <article class="item" style="top:409px">
      <div class="item__icon">
        <svg width="64" height="70" viewBox="0 0 64 70" fill="none" stroke="#b5541f" stroke-width="1.6" stroke-linecap="round">
          <line x1="10" y1="6" x2="36" y2="30"/>
          <circle cx="50" cy="20" r="6"/>
          <path d="M6 20 H50 L28 46 Z"/>
          <path d="M14 30 H42"/>
          <line x1="28" y1="46" x2="28" y2="64"/>
          <line x1="18" y1="65" x2="38" y2="65"/>
        </svg>
      </div>
      <h2 class="item__name">PASSIONISTA</h2>
      <p class="item__desc" style="top:45px">Vodka, Passionfruit Pulp, Mango Puree<br>Top up with Ginger &amp; Lemon Kombucha.</p>
      <div class="item__price">$17</div>
    </article>

    <div class="section-label" style="left:33px;top:530px">CRAFT BEER SPECIAL</div>
    <article class="item" style="top:553px">
      <div class="item__icon">
        <svg width="56" height="68" viewBox="0 0 56 68" fill="none" stroke="#b5541f" stroke-width="1.6" stroke-linecap="round" stroke-linejoin="round">
          <path d="M6 16 C2 12 6 4 12 6 C14 0 24 0 26 5 C30 1 38 3 37 9 C42 9 42 16 38 17 L38 22 M6 16 V64 H38 V17"/>
          <path d="M10 17 H34"/>
          <path d="M38 30 H46 C49 30 50 32 50 35 V50 C50 53 49 55 46 55 H38"/>
          <line x1="14" y1="28" x2="14" y2="58"/>
          <line x1="22" y1="28" x2="22" y2="58"/>
          <line x1="30" y1="28" x2="30" y2="58"/>
        </svg>
      </div>
      <h2 class="item__name" style="top:3px">SLY GECKO<br>FRUIT PUNCH</h2>
      <p class="item__desc" style="top:60px">Tropical Pale Ale - 4.8% Alc.</p>
      <div class="item__price">$10</div>
    </article>
  </section>
</div>
</body>
</html>
```